Regal Sweepers Brochure

Please see Attached is a Old Brochure of another company we owe, We need something like this with Regal Sweepers Logos and info
Lots of colors and picture of houses and family

Regal Sweepers
318 Corvin Avenue
Suite 27
Saint Paul, MN 55106
info@regalsweepersco.com
612-555-0193

Regal Sweepers
318 Corvin Avenue
Suite 27
Saint Paul, MN 55106
info@regalsweepersco.com
612-555-0193

Target Market(s)

Home Owners

Industry/Entity Type

It Company

Font styles to use
Serif

Requirements
Must have
• House picture Family picture lots pictures, Inside house pictures
Nice to have
• Please see Attached is a Old Brochure of another company we owe, We need something like this with Regal Sweepers Logos and info
• Lots of colors and picture of houses and family
• Regal Sweepers
• 318 Corvin Avenue
• Suite 27
• Saint Paul, MN 55106
• info@regalsweepersco.com
• 612-555-0193

```html
<!DOCTYPE html>
<html lang="en">
<head>
<meta charset="utf-8">
<title>Regal Sweepers Brochure</title>
<link rel="stylesheet" href="https://fonts.googleapis.com/css2?family=Arimo:wght@400;700&display=swap">
<style>
  :root {
    --yellow: #f6c430;
    --yellow-deep: #efb51f;
    --navy: #233a6e;
    --navy-dark: #1b2d57;
    --white: #ffffff;
    --ink: #1c1c1c;
    --backdrop: #efe7d8;
    --photo-room: #c9c7b8;
    --photo-lilac: #b9a9d6;
    --photo-house: #e9c86a;
    --photo-sky: #6ea6d8;
  }
  * { box-sizing: border-box; margin: 0; padding: 0; }
  html, body { width: 900px; height: 1200px; overflow: hidden; }
  body {
    background: var(--backdrop);
    font-family: "Arimo", Arial, sans-serif;
    color: var(--ink);
  }
  .canvas { position: relative; width: 900px; height: 1200px; overflow: hidden; }
  .spread {
    position: absolute; left: 20px; width: 860px; height: 560px;
    display: flex; box-shadow: 0 6px 18px rgba(0,0,0,.18);
  }
  .spread--inside { top: 26px; }
  .spread--outside { top: 614px; }
  .panel { position: relative; width: 286.67px; height: 560px; overflow: hidden; }
  .panel + .panel { border-left: 1px solid rgba(0,0,0,.08); }

  .photo { position: absolute; left: 0; width: 100%; }
  .photo--living { background: linear-gradient(160deg, #e8e6dc 0%, #b9b8ad 45%, #3d4a86 75%, #6b4a33 100%); }
  .photo--stairs { background: linear-gradient(180deg, #d8d6cc 0%, #a9a79a 60%, #8c8a80 100%); }
  .photo--bedroom { background: linear-gradient(160deg, #eef0e6 0%, #c7d0b6 50%, #8fa06a 100%); }
  .photo--kids-room { background: linear-gradient(180deg, #cfc4e6 0%, var(--photo-lilac) 55%, #d8c29c 100%); }
  .photo--shelves { background: linear-gradient(180deg, #e4eef4 0%, #b8cdd8 100%); }
  .photo--house { background: linear-gradient(180deg, var(--photo-sky) 0%, #9cc4e6 35%, var(--photo-house) 60%, #c98a3a 100%); }

  .yellow-block { position: absolute; background: var(--yellow); }
  .navy-bar {
    position: absolute; background: var(--navy); color: var(--white);
    font-weight: 700; text-align: center;
  }
  .section-tab {
    display: inline-block; background: var(--navy); color: var(--white);
    font-size: 10px; font-weight: 700; letter-spacing: .3px;
    padding: 4px 10px; border: 1.5px solid var(--white);
  }
  .body-copy { font-size: 8.4px; line-height: 1.32; text-align: justify; }
  .body-copy p + p { margin-top: 6px; }
  .body-copy strong { font-weight: 700; }

  .star-list { list-style: none; font-size: 11px; line-height: 1.35; }
  .star-list li { position: relative; padding-left: 16px; }
  .star-list li::before {
    content: "\2605"; position: absolute; left: 0; top: 0;
    color: var(--white); font-size: 10px;
  }

  /* Inside panel 1 */
  .intro .photo--living { top: 0; height: 150px; }
  .intro .yellow-block { top: 150px; left: 0; right: 0; height: 350px; padding: 10px 14px; }
  .intro .navy-bar { left: 0; right: 0; top: 500px; height: 60px; font-size: 12.5px; line-height: 1.3; padding-top: 13px; border-top: 3px solid var(--white); }

  /* Inside panel 2 */
  .standards { background: var(--yellow); }
  .standards .headline {
    position: absolute; top: 14px; left: 0; right: 0; background: var(--navy);
    color: var(--white); font-size: 10.5px; font-weight: 700; padding: 6px 12px; line-height: 1.3;
  }
  .standards .body-copy { position: absolute; top: 62px; left: 14px; right: 14px; }
  .standards .photo--stairs { top: 170px; height: 170px; }
  .standards .lead { position: absolute; top: 352px; left: 14px; right: 14px; font-size: 10px; font-weight: 700; }
  .standards .kitchen { position: absolute; top: 392px; left: 0; right: 0; }
  .standards .kitchen .section-tab { margin-left: 10px; font-size: 11px; }
  .standards .kitchen .star-list { margin: 8px 14px; font-size: 10px; }

  /* Inside panel 3 and outside panel 1 */
  .extras .photo--top { top: 0; height: 150px; }
  .extras .services { position: absolute; left: 0; right: 0; top: 150px; height: 240px; background: var(--yellow); padding: 10px 16px; }
  .extras .services .section-tab { display: block; margin: 0 -16px 10px; text-align: center; font-size: 11px; border-left: 0; border-right: 0; }
  .extras .photo--bottom { top: 390px; height: 170px; }

  /* Outside panel 2 */
  .details { background: var(--yellow); }
  .details .block { position: absolute; left: 12px; right: 12px; }
  .details .block .section-tab { margin-bottom: 6px; }
  .details .block--one { top: 12px; }
  .details .block--two { top: 186px; }
  .details .contact {
    position: absolute; left: 0; right: 0; bottom: 0; height: 128px;
    background: var(--navy); color: var(--white); text-align: center;
    clip-path: polygon(0 18%, 100% 0, 100% 100%, 0 100%);
    font-size: 9px; line-height: 1.4; padding-top: 36px;
  }
  .details .contact .section-tab {
    position: absolute; top: 14px; left: 50%; transform: translateX(-50%);
    background: var(--white); color: var(--navy); border: 0; font-size: 11px; font-weight: 400;
  }

  /* Outside panel 3 – cover */
  .cover { background: var(--white); }
  .cover .brand { position: absolute; top: 26px; left: 30px; display: flex; align-items: center; gap: 8px; }
  .cover .brand-mark { width: 26px; height: 26px; border-radius: 50%; background: var(--yellow); }
  .cover .brand-name { font-size: 19px; font-weight: 700; color: var(--navy); }
  .cover .tagline { position: absolute; top: 62px; left: 64px; font-size: 10px; color: var(--navy); }
  .cover .navy-field {
    position: absolute; left: 0; right: 0; top: 90px; height: 260px; background: var(--navy);
    clip-path: polygon(0 0, 100% 0, 100% 40%, 0 100%);
  }
  .cover .call { position: absolute; top: 132px; left: 30px; color: var(--white); }
  .cover .call-label { font-size: 15px; }
  .cover .call-number { font-size: 22px; margin-top: 4px; }
  .cover .photo--house {
    top: 190px; height: 370px;
    clip-path: polygon(0 42%, 100% 0, 100% 100%, 0 100%);
  }
</style>
</head>
<body>
<div class="canvas">

  <section class="spread spread--inside" aria-label="Brochure inside">
    <article class="panel intro">
      <div class="photo photo--living" role="img" aria-label="Bright living room with blue sofas and wooden coffee table"></div>
      <div class="yellow-block body-copy">
        <p>Regal Sweepers provides full House Cleaning Services to realtors, residential property managers, homeowners and renters in and around Minneapolis and Saint Paul, Minnesota. We are fully insured and proficient in handling our green cleaning products and equipment, and if you prefer, we can use your products too! Our pledge to you is that we'll get the job done and get it done right!</p>
        <p><strong>At Regal Sweepers LLC,</strong> we understand that every homeowner leads different lives and can't always keep up with the burden of having to clean out a house, whether they're too busy or just overwhelmed by their children! We were designed with the customer in mind!</p>
        <p>We make sure that your house is cleaned with attention to the smallest details. Our cleaners will leave your home, condo, apartment clean and fresh. Just tell us what exactly you want and the job will be done in no time with 100% satisfaction.</p>
        <p><strong>At Regal Sweepers,</strong> we understand that not every household is the same. We don't expect that every one needs the same services done on the same days. Everybody's different and so are we. That's why we offer very flexible scheduling for all our services.</p>
      </div>
      <div class="navy-bar">Our house cleaners are highly<br>motivated and well trained</div>
    </article>

    <article class="panel standards">
      <h2 class="headline">When it comes to cleaning, no concern is too small</h2>
      <div class="body-copy">
        <p>Whether you need us daily, weekly or monthly, we're here to help however we can.</p>
        <p>For the more extensive jobs we also offer green cleaning products and equipment, so your family can enjoy a fresh home that is safe for children and pets alike.</p>
      </div>
      <div class="photo photo--stairs" role="img" aria-label="Clean staircase and hallway inside a home"></div>
      <p class="lead">Our standard services include but are not limited to:</p>
      <div class="kitchen">
        <span class="section-tab">KITCHEN</span>
        <ul class="star-list">
          <li>Appliances</li>
          <li>Range</li>
          <li>Inside Microwave</li>
          <li>Handles</li>
          <li>Damp Wipe</li>
          <li>Clean Counter Surfaces</li>
        </ul>
      </div>
    </article>

    <article class="panel extras">
      <div class="photo photo--top photo--shelves" role="img" aria-label="Tidy white room with shelves and window"></div>
      <div class="services">
        <span class="section-tab">EXTRA SERVICES AVAILABLE</span>
        <ul class="star-list">
          <li>Garage cleaning and basements</li>
          <li>Cleaning blinds</li>
          <li>Move in/outs</li>
          <li>Wall cleaning</li>
          <li>Oven cleaning</li>
          <li>Cleaning refrigerators and freezers</li>
          <li>Frequency</li>
          <li>Weekly</li>
          <li>Bi-weekly</li>
          <li>Monthly</li>
          <li>One time</li>
        </ul>
      </div>
      <div class="photo photo--bottom photo--kids-room" role="img" aria-label="Lilac children's bedroom with wooden drawers"></div>
    </article>
  </section>

  <section class="spread spread--outside" aria-label="Brochure outside">
    <article class="panel extras">
      <div class="photo photo--top photo--bedroom" role="img" aria-label="Bright bedroom with green striped bedding"></div>
      <div class="services">
        <span class="section-tab">EXTRA SERVICES AVAILABLE</span>
        <ul class="star-list">
          <li>Garage cleaning and basements</li>
          <li>Cleaning blinds</li>
          <li>Move in/outs</li>
          <li>Wall cleaning</li>
          <li>Oven cleaning</li>
          <li>Cleaning refrigerators and freezers</li>
          <li>Frequency</li>
          <li>Weekly</li>
          <li>Bi-weekly</li>
          <li>Monthly</li>
          <li>One time</li>
        </ul>
      </div>
      <div class="photo photo--bottom photo--kids-room" role="img" aria-label="Lilac children's bedroom with wooden drawers"></div>
    </article>

    <article class="panel details">
      <div class="block block--one body-copy">
        <span class="section-tab">ONE CALL CLEANS IT ALL</span>
        <p>Your schedule may interfere with keeping a clean house, but your house is no match for our flexible scheduling! With our convenient arrangements, we will come as often as needed. It's up to you!</p>
        <p>Whether you need professional maid services daily, weekly, bi-weekly, one time or an occasional house-cleaning, we're there for you. If you've got a special occasion coming up, we will help. Moving can be stressful, we handle all of the deep cleaning to make your home shine! Whether you're renting a home or you're selling, we will make your life easier.</p>
      </div>
      <div class="block block--two body-copy">
        <span class="section-tab">HOUSE CLEANING ESTIMATES</span>
        <p>If you are tired of paying too much for your current house cleaning company, now is the time to give us a call. You will experience five STAR quality cleaning at a price that you can afford!</p>
        <p>To request a free estimate for your specific needs, please call 612-555-0193 today. We look forward to doing business with you!</p>
        <p>We understand every home is unique, so as you welcome us into your home we will already have a plan in mind. Our focus is knowing exactly what needs to be done keeping any additionally requested duties in mind and meeting all expectations as we stay systematically organized and on task.</p>
      </div>
      <address class="contact">
        <span class="section-tab">CONTACT US</span>
        Regal Sweepers<br>
        318 Corvin Avenue Suite 27<br>
        Saint Paul, MN 55106.<br>
        Phone: 612-555-0193<br>
        Email : info@regalsweepersco.com
      </address>
    </article>

    <article class="panel cover">
      <div class="brand">
        <span class="brand-mark"></span>
        <span class="brand-name">Regal Sweepers</span>
      </div>
      <p class="tagline">Professional Cleaning Service!</p>
      <div class="navy-field"></div>
      <div class="call">
        <p class="call-label">Call Us Today!</p>
        <p class="call-number">612-555-0193</p>
      </div>
      <div class="photo photo--house" role="img" aria-label="Yellow two-storey house with terracotta roof under blue sky"></div>
    </article>
  </section>

</div>
</body>
</html>
```